Venture Keeper's LanternBook

We need a cover design for a printed paperback book 8.5 inches by 11 inches. The book is a self-driven business planning process for people who wish to start or buy a business, be their own boss, entrepreneurs, small and home-based business owners. We hope for a design that is fun, with a treasure map flavor.

```html
<!DOCTYPE html>
<html lang="en">
<head>
<meta charset="utf-8">
<title>Venture Keeper's LanternBook — Cover</title>
<link rel="stylesheet" href="https://fonts.googleapis.com/css2?family=Bebas+Neue&family=Montserrat:wght@800&family=Open+Sans:wght@400;800&display=swap">
<style>
  :root {
    --backdrop: #dfe5e8;
    --cover-deep: #2660ab;
    --cover-mid: #2f74c0;
    --cover-sky: #5aaee9;
    --band-white: #ffffff;
    --title-blue: #2562ae;
    --text-white: #ffffff;
    --art-light: #e4e0d2;
    --art-shade: #c9d3da;
  }
  * { margin: 0; padding: 0; box-sizing: border-box; }
  html, body {
    width: 1200px;
    height: 1200px;
    overflow: hidden;
    background: var(--backdrop);
  }
  .book-cover {
    position: absolute;
    left: 170px;
    top: 44px;
    width: 860px;
    height: 1112px;
    overflow: hidden;
    background:
      radial-gradient(circle at 78% 30%, var(--cover-sky) 0%, rgba(90,174,233,0) 55%),
      linear-gradient(180deg, var(--cover-mid) 0%, var(--cover-deep) 100%);
  }
  .cover-illustration {
    position: absolute;
    left: 369px;
    top: 15px;
    width: 502px;
    height: 502px;
    border-radius: 50%;
    background: radial-gradient(circle at 40% 35%, var(--art-light) 0%, var(--art-shade) 100%);
  }
  .author-name {
    position: absolute;
    left: 127px;
    top: 92px;
    color: var(--text-white);
    font-family: "Open Sans", sans-serif;
    font-size: 62px;
    line-height: 1.12;
  }
  .author-name .first { font-weight: 400; display: block; }
  .author-name .last { font-weight: 800; display: block; }
  .title-line-one {
    position: absolute;
    left: 125px;
    top: 557px;
    color: var(--text-white);
    font-family: "Bebas Neue", sans-serif;
    font-size: 191px;
    line-height: 1;
    letter-spacing: 2px;
  }
  .title-band {
    position: absolute;
    left: 0;
    top: 734px;
    width: 687px;
    height: 176px;
    background: var(--band-white);
    border-radius: 0 10px 10px 0;
  }
  .title-line-two {
    position: absolute;
    left: 125px;
    top: 749px;
    color: var(--title-blue);
    font-family: "Bebas Neue", sans-serif;
    font-size: 170px;
    line-height: 1;
    letter-spacing: 1px;
  }
  .title-line-three {
    position: absolute;
    left: 127px;
    top: 925px;
    color: var(--text-white);
    font-family: "Montserrat", sans-serif;
    font-weight: 800;
    font-size: 84px;
    line-height: 1;
  }
</style>
</head>
<body>
  <main class="book-cover">
    <div class="cover-illustration" role="img" aria-label="Cartoon street-map globe with coloured roads, a navigation arrow and a green push pin against a blue sky"></div>
    <p class="author-name"><span class="first">AUTHOR</span><span class="last">NAME</span></p>
    <h1>
      <span class="title-line-one">VENTURE</span>
      <span class="title-band"></span>
      <span class="title-line-two">KEEPER'S</span>
      <span class="title-line-three">LANTERNBOOK</span>
    </h1>
  </main>
</body>
</html>
```